Wordpress Design

A full creative brief is enclosed as well as examples of websites that we feel appropiate for the client. The logo has been designed now, so its a matter of utilizing that brand, and creating a strong "less is more approach"

Better to have dropdowns and information on secondary pages than everything upfront.
Stylish, made in wordpress for easy updates and changes, architectually easy, HTML5 or later.. video compatable, along with severe database collection points.

Target Market(s)

business owners, sophisticated market, CEO's, corporates.Trendy.

Requirements
Must have
• video on opening page as a feature, login details for clients, take advantage of the full screen functionality of HTML5.
Drop downs on entry level 2 pages.
Space for carefully designed banner advertising.
Nice to have
• Full motion video, if we can. We have used templates with this in the past, it maybe too much at this stage however, but we will be creating a video on explainations, anyway.
Should not have
• constrained, or in frames. Not everything on the front page.

```html
<!DOCTYPE html>
<html lang="en">
<head>
<meta charset="utf-8">
<title>Stablemate – Racehorse Syndication</title>
<link rel="stylesheet" href="https://fonts.googleapis.com/css2?family=Arimo:wght@400;700&family=Questrial&display=swap">
<style>
  :root {
    --brand-blue: #1f8fd0;
    --brand-navy: #0f3a63;
    --nav-top: #1a9be0;
    --nav-bottom: #0b5b8e;
    --accent-yellow: #fff200;
    --panel-top: #1d4475;
    --panel-bottom: #263548;
    --card-top: #ffffff;
    --card-bottom: #c4c4c4;
    --text-dark: #222222;
    --text-body: #1e1e1e;
    --date-blue: #0e5b82;
    --footer-text: #444444;
    --header-top: #d6d6d6;
    --header-bottom: #ffffff;
  }
  * { box-sizing: border-box; margin: 0; padding: 0; }
  html, body { width: 1200px; height: 940px; overflow: hidden; background: #fff; }
  body { font-family: "Arimo", Arial, sans-serif; color: var(--text-body); position: relative; }

  .site-header {
    position: absolute; left: 0; top: 0; width: 1200px; height: 113px;
    background: linear-gradient(var(--header-top), var(--header-bottom));
  }
  .brand {
    position: absolute; left: 89px; top: 38px; display: flex; align-items: center; gap: 10px;
    font-family: "Arimo", Arial, sans-serif; font-weight: 700; font-size: 46px;
    color: var(--brand-navy); letter-spacing: -1.5px; line-height: 1;
  }
  .brand-mark { width: 18px; height: 18px; background: var(--brand-blue); }
  .client-login {
    position: absolute; left: 1006px; top: 20px; width: 106px; height: 31px;
    border-radius: 6px; border: 1px solid #9fb3c6;
    background: linear-gradient(#2c5a80, #0c2b48);
    color: #fff; font-weight: 700; font-size: 14px; line-height: 29px; text-align: center;
    box-shadow: 0 1px 2px rgba(0,0,0,.3);
  }
  .search {
    position: absolute; left: 885px; top: 66px; width: 226px; height: 29px;
    border-radius: 6px; border: 1px solid #bdbdbd; background: #fff;
    box-shadow: 1px 2px 2px rgba(0,0,0,.25);
    font-size: 13px; color: #777; padding: 6px 11px;
  }
  .search svg { position: absolute; right: 10px; top: 6px; }

  .main-nav {
    position: absolute; left: 0; top: 113px; width: 1200px; height: 50px;
    background: linear-gradient(var(--nav-top), var(--nav-bottom));
  }
  .main-nav ul { list-style: none; position: relative; height: 50px; }
  .main-nav li {
    position: absolute; top: 13px; height: 25px; line-height: 25px;
    color: #fff; font-weight: 700; font-size: 14px; white-space: nowrap;
  }
  .main-nav li.is-active { background: var(--accent-yellow); color: #111; padding: 0 10px; }

  .hero {
    position: absolute; left: 0; top: 163px; width: 1200px; height: 351px;
    background:
      linear-gradient(rgba(0,0,0,0) 55%, rgba(0,0,0,.15)),
      linear-gradient(#2f4a22 0%, #4f6b35 30%, #dfe6df 48%, #9bb36c 62%, #7fa04d 100%);
  }
  .hero-title {
    position: absolute; left: 88px; top: 178px;
    font-size: 37px; font-weight: 700; color: #fff; letter-spacing: -0.3px;
    text-shadow: 2px 3px 3px rgba(0,0,0,.6);
  }
  .hero-intro {
    position: absolute; left: 90px; top: 228px; width: 617px;
    font-size: 14px; font-weight: 700; line-height: 20px; color: #fff; text-align: justify;
    text-shadow: 1px 1px 2px rgba(0,0,0,.6);
  }

  .feature-panel {
    position: absolute; left: 88px; top: 544px; width: 1022px; height: 298px;
    border-radius: 14px; background: linear-gradient(var(--panel-top), var(--panel-bottom));
  }
  .card {
    position: absolute; top: 24px; width: 304px; height: 250px; border-radius: 14px;
    background: linear-gradient(var(--card-top), var(--card-bottom));
  }
  .card h2 {
    position: absolute; top: 20px; font-size: 22px; font-weight: 700;
    color: var(--text-dark); letter-spacing: -1px;
  }
  .card p { font-size: 13px; line-height: 22px; text-align: justify; color: var(--text-body); }
  .card-news { left: 25px; }
  .card-news h2 { left: 22px; }
  .news-item { position: absolute; left: 22px; width: 257px; }
  .news-date { font-family: "Questrial", "Century Gothic", sans-serif; font-size: 17px; color: var(--date-blue); line-height: 20px; }
  .news-item p { padding-left: 2px; }
  .card-why { left: 359px; }
  .card-why h2 { left: 27px; }
  .card-why p { position: absolute; left: 28px; top: 58px; width: 258px; }
  .card-newsletter { left: 692px; }
  .card-newsletter h2 { left: 29px; }
  .signup-label { position: absolute; left: 30px; top: 58px; font-size: 13px; }
  .email-field {
    position: absolute; left: 30px; top: 91px; width: 250px; height: 33px;
    background: #fff; border: 1px solid #c9c9c9;
    font-family: "Questrial", "Century Gothic", sans-serif; font-size: 16px; color: #111;
    padding: 6px 9px;
  }
  .signup-button {
    position: absolute; left: 31px; top: 145px; width: 85px; height: 32px; border-radius: 16px;
    background: linear-gradient(#ffff3a, #e8e800);
    box-shadow: 0 1px 2px rgba(0,0,0,.25);
    font-weight: 700; font-size: 15px; line-height: 32px; text-align: center; color: #111;
  }

  .footer-links {
    position: absolute; top: 864px; left: 0; width: 1227px; text-align: center;
    font-size: 11px; font-weight: 700; color: var(--footer-text);
  }
  .footer-links span { margin: 0 5px; }
  .copyright {
    position: absolute; top: 892px; left: 0; width: 1231px; text-align: center;
    font-size: 11px; font-weight: 700; color: var(--footer-text);
  }
</style>
</head>
<body>
  <header class="site-header">
    <div class="brand"><span class="brand-mark"></span>Stablemate</div>
    <div class="client-login">Client Login</div>
    <div class="search">Search
      <svg width="14" height="14" viewBox="0 0 14 14" aria-hidden="true">
        <circle cx="8.5" cy="5.5" r="4" fill="none" stroke="#2a5f9e" stroke-width="2"/>
        <line x1="5.5" y1="8.5" x2="1.5" y2="12.5" stroke="#2a5f9e" stroke-width="2.4" stroke-linecap="round"/>
      </svg>
    </div>
  </header>

  <nav class="main-nav">
    <ul>
      <li class="is-active" style="left:89px">About Us</li>
      <li style="left:223px">Community News</li>
      <li style="left:399px">Best of Breed</li>
      <li style="left:553px">Buying Syndication Shares</li>
      <li style="left:796px">Racing Information</li>
      <li style="left:986px">Joining Stablemate</li>
    </ul>
  </nav>

  <section class="hero" role="img" aria-label="Photograph of two jockeys racing thoroughbred horses on a grass track beside a white rail">
    <h1 class="hero-title">sharing racing with life</h1>
    <p class="hero-intro">When considering becoming a thoroughbred horse owner, there are many detailed processes to take into consideration when entering the racing industry.&nbsp; Racehorse ownership is an exciting experience that can build friendships, business networks; create wealth, knowledge of the industry and of course an incredible...</p>
  </section>

  <section class="feature-panel">
    <article class="card card-news">
      <h2>Latest News</h2>
      <div class="news-item" style="top:58px">
        <div class="news-date">12-05-2012</div>
        <p>Lorem Ipsum is simply dummy text of the printing and typesetting industry.</p>
      </div>
      <div class="news-item" style="top:140px">
        <div class="news-date">12-05-2012</div>
        <p>Lorem Ipsum is simply dummy text of the printing and typesetting industry.</p>
      </div>
    </article>

    <article class="card card-why">
      <h2>Why Us?</h2>
      <p>Our aim is to supplement that word of mouth with a website that helps customers who are interested in racehorse ownership understand their needs and discover what is important to them when choosing between particular syndicated horses.</p>
    </article>

    <article class="card card-newsletter">
      <h2>Newsletter Signup</h2>
      <div class="signup-label">Please enter your Email Id below</div>
      <div class="email-field">Enter Email Id Here</div>
      <div class="signup-button">SIGN UP</div>
    </article>
  </section>

  <footer>
    <div class="footer-links">About Us<span>|</span>Community News<span>|</span>Best of Breed<span>|</span>Buying Syndication Shares<span>|</span>Racing Information<span>|</span>Joining Stablemate</div>
    <div class="copyright">©&nbsp; 2012. All Rights Reserved.</div>
  </footer>
</body>
</html>
```